Health Information/Education Logo Design

We need a logo design for a new company based in Atlanta called Brightpath Care. The program is about patient empowerment. We provide health information and education on how to get healthy, stay healthy, and how to be proactive in your care. We also provide medication and injection training to help patients feel their best and to ensure successful therapy outcomes.
We like the colors yellow, pink, teal and purple and would like to see some or all of these colors in the designs. The final design should communicate caring, considerate, compassionate information, education and training services
Education
Contact Information for Business Card
Brightpath Care
Lorraine Pettaway RN, MSN, MHA
Nurse Educator
404.555.0187 cell
404.555.0142 fax

```html
<!DOCTYPE html>
<html lang="en">
<head>
<meta charset="utf-8">
<title>Brightpath Care – Business Card</title>
<link href="https://fonts.googleapis.com/css2?family=Lato:wght@400;700&display=swap" rel="stylesheet">
<style>
  :root {
    --page-bg: #ecebee;
    --purple: #6a4fa8;
    --purple-light: #8a72c2;
    --purple-dark: #5a3f98;
    --pink: #e0358f;
    --white: #ffffff;
    --ink: #2d2d2d;
  }
  * { margin: 0; padding: 0; box-sizing: border-box; }
  html, body {
    width: 1200px; height: 891px; overflow: hidden;
    background: var(--page-bg);
    font-family: "Lato", Arial, sans-serif;
  }
  .canvas { position: relative; width: 1200px; height: 891px; }

  .card {
    position: absolute;
    width: 560px; height: 320px;
    border-radius: 14px;
    overflow: hidden;
    box-shadow: 0 10px 28px rgba(0,0,0,0.18);
  }

  /* Front */
  .card-front {
    left: 90px; top: 110px;
    background: linear-gradient(160deg, var(--purple-light) 0%, var(--purple) 45%, var(--purple-dark) 100%);
    display: flex; align-items: center; justify-content: center;
  }
  .brand {
    display: flex; align-items: center; gap: 14px;
  }
  .brand-dot {
    width: 34px; height: 34px; border-radius: 50%;
  }
  .brand-name {
    font-weight: 700; letter-spacing: 0.5px; white-space: nowrap;
  }
  .card-front .brand-dot { background: var(--white); }
  .card-front .brand-name { color: var(--white); font-size: 36px; }

  /* Back */
  .card-back {
    left: 550px; top: 470px;
    background: var(--white);
    border-radius: 4px;
  }
  .card-back .brand {
    position: absolute; left: 36px; top: 138px; gap: 10px;
  }
  .card-back .brand-dot { width: 24px; height: 24px; background: var(--pink); }
  .card-back .brand-name { color: var(--purple); font-size: 22px; }

  .contact-person {
    position: absolute; left: 300px; top: 46px;
  }
  .person-name {
    color: var(--purple); font-size: 17px; font-weight: 400;
  }
  .person-title {
    color: var(--pink); font-size: 11px; margin-top: 6px;
  }
  .contact-lines {
    position: absolute; left: 316px; top: 128px;
    font-size: 11.5px; color: var(--ink); line-height: 22px;
  }
  .contact-lines .label { color: var(--purple); display: inline-block; width: 16px; }

  .web-band {
    position: absolute; left: 0; right: 0; top: 226px; height: 50px;
    background: var(--purple);
    display: flex; align-items: center; justify-content: center;
    color: var(--white); font-size: 17px; letter-spacing: 7px;
  }
  .rule {
    position: absolute; left: 0; right: 0; height: 3px; background: var(--pink);
  }
  .rule-top { top: 216px; }
  .rule-bottom { top: 283px; }
</style>
</head>
<body>
<main class="canvas">

  <section class="card card-front" aria-label="Business card front">
    <div class="brand">
      <span class="brand-dot"></span>
      <span class="brand-name">Brightpath Care</span>
    </div>
  </section>

  <section class="card card-back" aria-label="Business card back">
    <div class="contact-person">
      <p class="person-name">Lorraine Pettaway RN, MSN</p>
      <p class="person-title">MHA Nurse Educator</p>
    </div>
    <div class="contact-lines">
      <p><span class="label">M</span>: 404.555.0187</p>
      <p><span class="label">F</span>: 404.555.0142</p>
    </div>
    <div class="brand">
      <span class="brand-dot"></span>
      <span class="brand-name">Brightpath Care</span>
    </div>
    <div class="rule rule-top"></div>
    <div class="web-band">www.brightpathcare.com.au</div>
    <div class="rule rule-bottom"></div>
  </section>

</main>
</body>
</html>
```